Technology Solutions Provider

Let’s design a business card that will be as simple and bold at the same time. Name, email address, website & phone number.

Target Market(s)

Small to Medium Size Business

Industry/Entity Type

It Professional

Contact Information for Business Card

Name, email, website, phone numbers

Font styles to use
Sans Serif

Colors
ec1f27
f04a50
dddddd
919191
000000
ffffff

Requirements
Must have
• Clean simple look using my existing logo. I just need to the basic contact information on this card.
Nice to have
• Im considering the square size card versus the standard size business card.
Should not have
• No Mailing Address, no list of services.

```html
<!DOCTYPE html>
<html lang="en">
<head>
<meta charset="UTF-8">
<title>Kora Systems – Business Card</title>
<link rel="stylesheet" href="https://fonts.googleapis.com/css2?family=Saira:wght@400;600&display=swap">
<style>
  :root {
    --red: #ec1f27;
    --red-soft: #f04a50;
    --light: #dddddd;
    --grey: #919191;
    --black: #000000;
    --white: #ffffff;
    --stage-top: #3c3c3c;
    --stage-bottom: #525252;
    --card-dark: #141414;
  }
  * { margin: 0; padding: 0; box-sizing: border-box; }
  html, body { width: 1200px; height: 900px; overflow: hidden; }
  body {
    position: relative;
    background: linear-gradient(180deg, var(--stage-top) 0%, var(--stage-bottom) 100%);
    font-family: "Saira", Arial, sans-serif;
  }
  .card {
    position: absolute;
    top: 306px;
    width: 440px;
    height: 271px;
    border-radius: 12px;
    overflow: hidden;
  }
  .card-front { left: 149px; background: var(--white); }
  .card-back { left: 608px; background: var(--card-dark); }

  .brand {
    position: absolute;
    right: 25px;
    top: 60px;
    text-align: right;
  }
  .brand-name {
    font-size: 22px;
    font-weight: 600;
    color: var(--red);
    line-height: 1;
    letter-spacing: 0.3px;
  }
  .brand-tagline {
    margin-top: 3px;
    font-size: 10px;
    color: var(--grey);
    line-height: 1;
  }

  .holder {
    position: absolute;
    left: 22px;
    top: 153px;
    width: 393px;
  }
  .holder-name {
    display: flex;
    align-items: center;
    gap: 16px;
    font-size: 14.5px;
    font-weight: 600;
    color: var(--red);
    letter-spacing: 0.4px;
    line-height: 18px;
    text-transform: uppercase;
  }
  .holder-name::after {
    content: "";
    flex: 1;
    height: 1px;
    background: var(--black);
  }
  .holder-role {
    font-size: 12.5px;
    color: var(--black);
    line-height: 15px;
  }

  .contact-list {
    position: absolute;
    right: 23px;
    top: 192px;
    list-style: none;
    text-align: right;
  }
  .contact-item {
    display: flex;
    justify-content: flex-end;
    align-items: center;
    gap: 5px;
    font-size: 13px;
    color: var(--black);
    line-height: 16px;
  }
  .contact-icon { width: 9px; height: 9px; fill: var(--red); }

  .back-pattern {
    position: absolute;
    inset: 0;
    background: linear-gradient(180deg, #111111 0%, #1a1a1a 50%, #121212 100%);
  }
  .back-mark {
    position: absolute;
    left: 0;
    right: 0;
    top: 133px;
    text-align: center;
    font-size: 20px;
    font-weight: 400;
    color: var(--red);
    line-height: 1;
    letter-spacing: 0.5px;
  }
</style>
</head>
<body>
  <section class="card card-front">
    <div class="brand">
      <div class="brand-name">kora systems</div>
      <div class="brand-tagline">technology solutions provider</div>
    </div>

    <div class="holder">
      <div class="holder-name">Daniel Hart</div>
      <div class="holder-role">Managing Director</div>
    </div>

    <ul class="contact-list">
      <li class="contact-item">(044)987654321
        <svg class="contact-icon" viewBox="0 0 10 10"><path d="M2 0.5 L3.6 2.6 L2.8 3.6 Q4 5.8 6.3 7.2 L7.4 6.4 L9.5 8 L8.3 9.5 Q3.5 9 0.5 1.8 Z"/></svg>
      </li>
      <li class="contact-item">hello@korasystems.com
        <svg class="contact-icon" viewBox="0 0 10 10"><path d="M0.5 2 H9.5 V8 H0.5 Z M0.9 2.4 L5 5.6 L9.1 2.4" stroke="#fff" stroke-width="0.8"/></svg>
      </li>
      <li class="contact-item">www.korasystems.com
        <svg class="contact-icon" viewBox="0 0 10 10"><circle cx="5" cy="5" r="4.5"/><path d="M0.8 5 H9.2 M5 0.6 Q2.6 5 5 9.4 M5 0.6 Q7.4 5 5 9.4" stroke="#fff" stroke-width="0.7" fill="none"/></svg>
      </li>
    </ul>
  </section>

  <section class="card card-back">
    <div class="back-pattern" role="img" aria-label="Faint repeating brand-name pattern on a dark background"></div>
    <div class="back-mark">kora</div>
  </section>
</body>
</html>
```